Wordpress and Elementor Pro website

We need a Wordpress/Elementor Pro design for our website. We already have a logo design and installed Wordpress. We have some ideas concerning the design, and we will share two websites. Both the design and content placement we like about these websites. We would like to see designs that use the color Purple (the same as the logo color), white and black. We provide these services: SEO optimization, SEO copywriting and online campaigns. We will provide a list of the page's we would like to see in the design.

Target Market(s)

Entrepreneurs, business owners. Companies who would like to expand online with texts and SEO.

Industry/Entity Type

Digital Marketing

Coding

Coded - Design and coding required

Number of Pages Required

5+ page

Font styles to use
Sans Serif

Colors
886aae
fffefd
0355a3

Requirements
Must have
• Single pages and singel posts of Elementor so I can create new pages and blog posts in the future.

```html
<!DOCTYPE html>
<html lang="nl">
<head>
<meta charset="utf-8">
<title>Groeiwerk Studio</title>
<link rel="stylesheet" href="https://fonts.googleapis.com/css2?family=Montserrat:wght@400;500;600;700;800&display=swap">
<style>
:root{
  --purple:#6a3597;
  --purple-dark:#52217f;
  --purple-brand:#7a3fa8;
  --ink:#1f2a37;
  --text:#333a44;
  --muted:#8a8f98;
  --band:#f3f9fc;
  --white:#ffffff;
  --lavender:#e7dcf2;
  --footer:#16293a;
  --wave-grey:#d6d6d6;
}
*{margin:0;padding:0;box-sizing:border-box}
html,body{width:1200px;height:4545px;overflow:hidden;background:var(--white)}
body{position:relative;font-family:'Montserrat',sans-serif;color:var(--text)}
.abs{position:absolute}

/* header */
.brand{left:232px;top:30px;width:180px;text-align:center}
.brand-mark{display:block;width:54px;height:54px;margin:0 auto 8px;border:3px solid var(--purple-brand);border-radius:6px}
.brand-name{font-size:25px;font-weight:500;color:var(--purple-brand);letter-spacing:1px;line-height:1}
.brand-sub{font-size:8px;font-weight:500;color:var(--purple-brand);letter-spacing:5px;margin-top:4px}
.nav{top:57px;left:484px;display:flex;align-items:center;font-size:11px;font-weight:700;letter-spacing:1px;color:var(--ink)}
.nav a{color:inherit;text-decoration:none;margin-right:32px}
.nav a.active{color:var(--purple-brand)}
.nav .sep{width:1px;height:14px;background:#c9c9c9;margin-right:20px}

/* services */
.service{top:212px;width:230px}
.service h3{font-size:11.5px;font-weight:700;letter-spacing:1px;color:var(--ink);margin-bottom:12px}
.service p{font-size:9.5px;line-height:17px;color:var(--text)}
.headline{left:232px;top:408px;font-size:38px;font-weight:800;letter-spacing:3px;line-height:45px;color:var(--ink);text-transform:uppercase}

/* clients */
.clients{left:0;top:632px;width:1200px;height:345px;background:var(--band)}
.client{width:150px;text-align:center;font-size:19px;font-weight:700;color:var(--ink);letter-spacing:.5px}

/* about */
.name-panel{left:234px;top:1063px;width:326px;height:342px;background:var(--purple-brand)}
.name-vertical{left:232px;top:1220px;width:80px;transform:rotate(-90deg);color:var(--white);font-size:21px;font-weight:700;letter-spacing:3px;white-space:nowrap;text-align:center}
.portrait{left:302px;top:1080px;width:282px;height:342px;background:linear-gradient(160deg,#c9b8a6,#8d7868 55%,#4a4a52)}
.about{left:654px;top:1070px;width:316px}
.about h2{font-size:26px;font-weight:600;color:var(--ink);letter-spacing:1px;margin-bottom:18px}
.about .lead{font-size:12px;font-weight:600;line-height:20px;color:var(--ink);text-align:justify;margin-bottom:20px}
.about p{font-size:9.5px;line-height:20px;text-align:justify;margin-bottom:20px}

/* pillars */
.pillar{width:236px;text-align:center}
.pillar .icon{width:70px;height:70px;margin:0 auto 14px;border-radius:50%;background:var(--purple-brand)}
.pillar h3{font-size:26px;font-weight:600;color:var(--ink);margin-bottom:12px}
.pillar p{font-size:9.5px;line-height:20px}

/* purple section */
.wave{left:0;top:1870px}
.purple-field{left:0;top:1990px;width:1200px;height:2290px;background:var(--purple)}
.col-head{height:45px;background:var(--white);color:var(--purple-brand);font-size:26px;font-weight:700;padding:6px 20px;line-height:33px}
.spine{left:292px;top:2233px;width:3px;height:1774px;background:var(--white)}
.connector{left:697px;top:2185px;width:4px;height:1901px;background:var(--white)}
.node{left:238px;width:112px;height:112px;border-radius:50%;background:var(--white);display:flex;align-items:center;justify-content:center}
.node .icon{width:70px;height:70px;border-radius:50%;background:var(--lavender)}
.label{left:350px;width:262px;height:45px;background:var(--purple-dark);color:var(--white);font-size:19px;font-weight:700;display:flex;align-items:center;padding-left:22px;line-height:23px}
.label.two{height:68px}
.req{left:612px;width:352px;background:var(--white);color:#222;font-size:16px;font-weight:500;line-height:20.5px;padding:14px 22px;display:flex;flex-direction:column;justify-content:center}
.req p+p{margin-top:5px}
.cta{left:478px;top:4150px;width:244px;height:62px;border-radius:31px;background:var(--white);color:var(--purple-dark);font-size:18px;font-weight:700;letter-spacing:1px;display:flex;align-items:center;justify-content:center}

/* footer */
.footer{left:0;top:4280px;width:1200px;height:265px;background:var(--footer);color:var(--white)}
.fcol{top:56px;font-size:11px;font-weight:500;line-height:27px}
.copyright{left:0;top:212px;width:1200px;text-align:center;font-size:10px;color:#c7ccd3}
</style>
</head>
<body>

<header>
  <div class="abs brand">
    <span class="brand-mark"></span>
    <div class="brand-name">GROEIWERK</div>
    <div class="brand-sub">STUDIO</div>
  </div>
  <nav class="abs nav">
    <a class="active" href="#">HOME</a><a href="#">SERVICES</a><a href="#">CASES</a><a href="#">ABOUT US</a><a href="#">CONTACT</a><span class="sep"></span><a href="#">EN ▾</a>
  </nav>
</header>

<section>
  <div class="abs service" style="left:232px"><h3>SEO COPYWRITING</h3><p>Lorem ipsum dolor sit amet, consectetur adipiscing elit. In quam lorem, porttitor et varius sit amet, placerat id elit. Curabitur rutrum ante vel turpis tincidunt, id elementum libero sodales.</p></div>
  <div class="abs service" style="left:484px"><h3>SEARCH ENGINE OPTIMIZATION</h3><p>Lorem ipsum dolor sit amet, consectetur adipiscing elit. In quam lorem, porttitor et varius sit amet, placerat id elit. Curabitur rutrum ante vel turpis tincidunt, id elementum libero sodales.</p></div>
  <div class="abs service" style="left:735px"><h3>ONLINE CAMPAIGNS</h3><p>Lorem ipsum dolor sit amet, consectetur adipiscing elit. In quam lorem, porttitor et varius sit amet, placerat id elit. Curabitur rutrum ante vel turpis tincidunt, id elementum libero sodales.</p></div>
  <h1 class="abs headline">Omdat online groeien in<br>omzet en winst een<br>specialisme is.</h1>
</section>

<section class="abs clients">
  <div class="abs client" style="left:210px;top:118px">Northwind</div>
  <div class="abs client" style="left:367px;top:118px">Halvorsen</div>
  <div class="abs client" style="left:523px;top:118px">Brightfield</div>
  <div class="abs client" style="left:680px;top:118px">Kestrel</div>
  <div class="abs client" style="left:837px;top:118px">Ovida</div>
  <div class="abs client" style="left:210px;top:206px">Marlow Tech</div>
  <div class="abs client" style="left:367px;top:206px">Fernleaf</div>
  <div class="abs client" style="left:523px;top:206px">Quarry Data</div>
  <div class="abs client" style="left:680px;top:206px">Tidewell</div>
  <div class="abs client" style="left:837px;top:206px">Plainly</div>
</section>

<section>
  <div class="abs name-panel"></div>
  <div class="abs name-vertical">DAAN VERHOEF</div>
  <div class="abs portrait" role="img" aria-label="Portretfoto van Daan Verhoef aan zijn bureau met een kop koffie"></div>
  <div class="abs about">
    <h2>About Us</h2>
    <p class="lead">Etiam ut sapien enim. Etiam facilisis dictum iaculis. Suspendisse sollicitudin sem quis dui vulputate sagittis.</p>
    <p>Lorem ipsum dolor sit amet, consectetur adipiscing elit. In quam lorem, porttitor et varius sit amet, placerat id elit. Curabitur rutrum ante vel turpis tincidunt, id elementum libero sodales. Vestibulum auctor massa sed lacus lobortis, vel varius dui aliquet. Duis non dapibus enim, sed condimentum sapien. Maecenas ut iaculis ligula. Nam at iaculis lorem. In hac habitasse platea dictumst. Aliquam erat volutpat.</p>
    <p>Praesent interdum fringilla velit, nec dapibus nulla dictum vel. Nam vel efficitur felis.</p>
  </div>

  <div class="abs pillar" style="left:230px;top:1525px"><div class="icon" role="img" aria-label="Icoon gloeilamp voor strategie"></div><h3>Strategy</h3><p>Etiam ut sapien enim. Etiam facilisis dictum iaculis. Suspendisse sollicitudin sem quis dui vulputate sagittis. Vivamus quis nibh quis augue convallis tincidunt.</p></div>
  <div class="abs pillar" style="left:480px;top:1600px"><div class="icon" role="img" aria-label="Icoon netwerk met wereldbol voor verkeer"></div><h3>Traffic</h3><p>Etiam ut sapien enim. Etiam facilisis dictum iaculis. Suspendisse sollicitudin sem quis dui vulputate sagittis. Vivamus quis nibh quis augue convallis tincidunt.</p></div>
  <div class="abs pillar" style="left:732px;top:1525px"><div class="icon" role="img" aria-label="Icoon grafiek voor conversie"></div><h3>Conversion</h3><p>Etiam ut sapien enim. Etiam facilisis dictum iaculis. Suspendisse sollicitudin sem quis dui vulputate sagittis. Vivamus quis nibh quis augue convallis tincidunt.</p></div>
</section>

<section>
  <svg class="abs wave" width="1200" height="140" viewBox="0 0 1200 140" aria-hidden="true">
    <path d="M0 110 C180 50 300 10 430 20 C560 30 620 120 760 118 C900 116 1020 40 1200 38 L1200 140 L0 140 Z" fill="var(--wave-grey)"/>
    <path d="M0 130 C180 70 300 35 430 40 C560 45 620 125 760 124 C900 123 1020 60 1200 50 L1200 140 L0 140 Z" fill="var(--purple)"/>
  </svg>
  <div class="abs purple-field"></div>

  <div class="abs col-head" style="left:237px;top:2097px;width:195px">Onderdelen</div>
  <div class="abs col-head" style="left:612px;top:2095px;width:166px">Vereisten</div>

  <div class="abs spine"></div>
  <div class="abs connector"></div>

  <!-- rows -->
  <div class="abs node" style="top:2177px"><div class="icon" role="img" aria-label="Icoon handen met pakket"></div></div>
  <div class="abs label two" style="top:2199px">Productpagina's of diensten</div>
  <div class="abs req" style="top:2185px;height:92px"><p>Kolommen of alinea's met subkopjes. Per product de juiste productspecificaties.</p></div>

  <div class="abs node" style="top:2318px"><div class="icon" role="img" aria-label="Icoon blogpagina"></div></div>
  <div class="abs label" style="top:2352px">Blog</div>
  <div class="abs req" style="top:2300px;height:150px"><p>Helpt enorm om verbinding te leggen met de doelgroep en bezoekers vanuit Searchly te trekken. Alleen inzetten als het blog structureel wordt bijgehouden en gereageerd op reacties</p></div>

  <div class="abs node" style="top:2604px"><div class="icon" role="img" aria-label="Icoon pen en tekst"></div></div>
  <div class="abs label" style="top:2638px">Teksten</div>
  <div class="abs req" style="top:2476px;height:369px"><p>Goed geschreven. Taal, stijl, interpunctie, zinslengte en signaalwoorden. Klantgericht: Interessant om te lezen en relevant. Pas opsommingen toe waar mogelijk.</p><p>Actiegericht: Schrijf teksten gericht op het doel dat je hebt met je bezoeker. Help je bezoeker om het door hem gezochte product te vinden en in contact te komen met de juiste medewerker.</p><p>CTA's: Call To Actions. Voorbeelden: demo-aanvraag, brochure aanvragen, webinar-inschrijving, ebook, whitepaper etc.</p></div>

  <div class="abs node" style="top:2839px"><div class="icon" role="img" aria-label="Icoon letters"></div></div>
  <div class="abs label" style="top:2873px">Aantal woorden</div>
  <div class="abs req" style="top:2872px;height:48px"><p>Minimaal 500 per pagina</p></div>

  <div class="abs node" style="top:2992px"><div class="icon" role="img" aria-label="Icoon zoeken met sleutel"></div></div>
  <div class="abs label" style="top:3026px">Zoekwoorden</div>
  <div class="abs req" style="top:2942px;height:207px"><p>LSI zoekwoorden (bijv. naast "hondenvoer kopen" bijvoorbeeld "puppievoer kopen"). De winst zit vaak in het scoren op langere zoekwoorden, waar minder op wordt geconcurreerd.</p><p>Belangrijkste zoekwoord in H1 en H2 titels en eerste alinea.</p></div>

  <div class="abs node" style="top:3140px"><div class="icon" role="img" aria-label="Icoon plug-in module"></div></div>
  <div class="abs label" style="top:3174px">Plug-ins</div>
  <div class="abs req" style="top:3173px;height:50px"><p>RankPilot SEO</p></div>

  <div class="abs node" style="top:3276px"><div class="icon" role="img" aria-label="Icoon monitor met code"></div></div>
  <div class="abs label" style="top:3310px">Technisch</div>
  <div class="abs req" style="top:3286px;height:92px"><p>On page: korte URL's, title tag en metadescription. Sitemap. Snelle laadtijd.</p></div>

  <div class="abs node" style="top:3421px"><div class="icon" role="img" aria-label="Icoon redactie op scherm"></div></div>
  <div class="abs label" style="top:3455px">Redactie</div>
  <div class="abs req" style="top:3435px;height:77px"><p>Het samenbrengen van webdesign met de teksten</p></div>

  <div class="abs node" style="top:3576px"><div class="icon" role="img" aria-label="Icoon vogel op scherm"></div></div>
  <div class="abs label two" style="top:3598px">Bounce rate en dwell time</div>
  <div class="abs req" style="top:3541px;height:197px"><p>Bounce Rate monitoren, zo laag mogelijkhouden. Kun je meten met Searchly Analytics. Met Searchly Console kun je monitoren op welke zoekwoorden je wordt gevonden.</p><p>Dwell time houdt in hoe lang mensen op je pagina blijven.</p></div>

  <div class="abs node" style="top:3769px"><div class="icon" role="img" aria-label="Icoon schakels"></div></div>
  <div class="abs label" style="top:3803px">Interne links</div>
  <div class="abs req" style="top:3766px;height:119px"><p>In teksten linken naar andere pagina's. Zo ziet Searchly welke onderwerpen met elkaar verbonden zijn</p></div>

  <div class="abs node" style="top:3951px"><div class="icon" role="img" aria-label="Icoon netwerk van personen"></div></div>
  <div class="abs label" style="top:3985px">Externe links/backlinks</div>
  <div class="abs req" style="top:3911px;height:175px"><p>Iedere verwijzing van een andere website is als het ware "een stem" zoals bij verkiezingen. Hoe meer relevante links van waardevolle en vergelijkbare websites, hoe sterker je domeinscore en beter Searchly je zal ranken in hun lijst.</p></div>

  <a class="abs cta">CONTACT US</a>
</section>

<footer class="abs footer">
  <div class="abs fcol" style="left:232px">Cookie Policy<br>Disclaimer<br>Privacy Policy</div>
  <div class="abs fcol" style="left:390px">VAT No.: NL000111222<br>CoC No.: 11223344</div>
  <div class="abs fcol" style="left:586px">Address:<br><span style="line-height:18px;display:block;margin-top:4px">Molenpad 7, 4321 AB,<br>Leerdam</span></div>
  <div class="abs fcol" style="left:792px">+31 (0)10-555 0199<br>info@groeiwerkstudio.nl</div>
  <div class="abs copyright">Copyright © 2020 Groeiwerk Studio. All Rights Reserved.</div>
</footer>

</body>
</html>
```